FOR SALE sign for REAL ESTATE BROKERAGE

Hello - our sign is attached. Need to make it part of FOR SALE sign. Think TERA/VOX, Dunmore Pratt, Foxglen Ashworth. Needs to have logo + FOR SALE + company website and phone number Its 24 x 30 standard size Needs to be MODERN yet luxury / sophisticated. Colors = red, black, gray, white (any mix). Will be used all over Philadelphia + surrounding areas. Please do Qwindle Image search on FOR SALE SIGNGS for some top comanies- Tera/vox, dunmore pratt, foxglen ashworth *** please mock-up the sign in front of a house

Target Market(s)

People with $$

Industry/Entity Type

Real Estate

Font styles to use
Sans Serif

Colors
ec1f27
ffffff
000000
5c5c5c

Requirements
Must have
• logo, website (tallpinehomes.example) phone number 555-014-7390 Agent name: Dorin Maklasov

```html
<!DOCTYPE html>
<html lang="en">
<head>
<meta charset="utf-8">
<title>Tallpine Homes – For Sale Sign</title>
<link href="https://fonts.googleapis.com/css2?family=Lato:wght@700;900&family=Roboto+Condensed:wght@700&display=swap" rel="stylesheet">
<style>
  :root {
    --brand-red: #c01f2f;
    --ink: #222222;
    --white: #ffffff;
    --page: #ffffff;
    --grey: #5c5c5c;
  }
  * { margin: 0; padding: 0; box-sizing: border-box; }
  html, body { width: 803px; height: 1200px; overflow: hidden; background: var(--page); }
  .canvas { position: relative; width: 803px; height: 1200px; }

  .sign {
    position: absolute; left: 51px; top: 320px;
    width: 700px; height: 560px;
    background: var(--white);
    border-radius: 22px;
    box-shadow: 0 4px 14px rgba(0,0,0,0.22);
  }
  .sign-face {
    position: absolute; inset: 19px;
    border-radius: 18px; overflow: hidden;
    background: var(--brand-red);
  }
  .sign-top { position: absolute; left: 0; top: 0; right: 0; height: 254px; background: var(--ink); }
  .sign-divider { position: absolute; left: 0; right: 0; top: 254px; height: 3px; background: var(--white); }

  .headline {
    position: absolute; left: 0; right: 0; top: 42px;
    text-align: center;
    font-family: "Lato", sans-serif; font-weight: 900;
    font-size: 126px; line-height: 1; letter-spacing: -2px;
    color: var(--white);
  }

  .company-panel {
    position: absolute; left: 129px; top: 190px;
    width: 441px; height: 197px;
    background: var(--white); border-radius: 16px;
    display: flex; flex-direction: column; align-items: center; justify-content: center;
    gap: 18px;
  }
  .company-name {
    display: flex; align-items: center; gap: 12px;
    font-family: "Lato", sans-serif; font-weight: 900;
    font-size: 44px; line-height: 1; letter-spacing: -0.5px;
    color: var(--brand-red);
  }
  .company-mark { width: 26px; height: 26px; background: var(--brand-red); flex: none; }
  .agent-name {
    font-family: "Lato", sans-serif; font-weight: 700;
    font-size: 24px; line-height: 1; letter-spacing: 4px;
    color: var(--grey); text-transform: uppercase;
  }

  .phone {
    position: absolute; left: 0; right: 0; top: 404px;
    text-align: center;
    font-family: "Roboto Condensed", sans-serif; font-weight: 700;
    font-size: 76px; line-height: 1; color: var(--white);
  }
  .website {
    position: absolute; left: 0; right: 0; top: 486px;
    text-align: center;
    font-family: "Lato", sans-serif; font-weight: 700;
    font-size: 32px; line-height: 1; color: var(--white);
  }
  .website .domain { color: var(--ink); }
</style>
</head>
<body>
<div class="canvas">
  <div class="sign">
    <div class="sign-face">
      <div class="sign-top"></div>
      <div class="sign-divider"></div>
    </div>
    <div class="headline">FOR SALE</div>
    <div class="company-panel">
      <div class="company-name"><span class="company-mark"></span>Tallpine Homes</div>
      <div class="agent-name">Dorin Maklasov</div>
    </div>
    <div class="phone">(555) 014-7390</div>
    <div class="website">www.<span class="domain">tallpinehomes</span>.example</div>
  </div>
</div>
</body>
</html>
```